Corvalt Web design

I described what I need to the doc.
Please see the my request from the following URL.
http://marblefox204.tundo.jp/CorvaltHPdraft.pdf

Please see my request and don't suggest boring typical web.

We need the innovation and the unique suggestion from you.

The log updated the site. 

Please see and design on your mind.

Thanks
corvalt

The flag on countries are for changing language.
It must be small, all designs are big.

Seeing the logo image, the we must be cool with white/black/grey.
Most designs are colorful or for kids.

```html
<!DOCTYPE html>
<html lang="en">
<head>
<meta charset="utf-8">
<title>Corvalt</title>
<link rel="stylesheet" href="https://fonts.googleapis.com/css2?family=Signika:wght@600;700&display=swap">
<style>
  :root {
    --bg-center: #ffffff;
    --bg-edge: #d3d3d3;
    --tab-fill: #dcdcdc;
    --nav-light: #a2a2a2;
    --nav-dark: #4f4f4f;
    --brand: #505050;
    --brand-mark: #6a6a6a;
    --flag-red: #d52b1e;
    --flag-blue: #233a7a;
    --flag-yellow: #ffde00;
    --flag-white: #ffffff;
  }
  * { margin: 0; padding: 0; box-sizing: border-box; }
  html, body { width: 1200px; height: 751px; overflow: hidden; }
  body {
    position: relative;
    font-family: "Signika", "Trebuchet MS", sans-serif;
    background: radial-gradient(ellipse 60% 70% at 50% 45%, var(--bg-center) 0%, #f1f1f1 40%, var(--bg-edge) 100%);
  }
  .language-tab {
    position: absolute;
    left: 453px; top: 0;
    width: 282px; height: 81px;
    background: var(--tab-fill);
    border-radius: 0 0 40px 40px;
    display: flex;
    justify-content: center;
    align-items: center;
    gap: 23px;
    padding-bottom: 4px;
  }
  .language-tab a { display: block; width: 48px; height: 34px; box-shadow: 0 1px 2px rgba(0,0,0,.35); }
  .language-tab svg { display: block; width: 100%; height: 100%; }
  .main-nav a {
    position: absolute;
    top: 362px;
    font-size: 38px;
    line-height: 1;
    font-weight: 700;
    letter-spacing: -1px;
    text-decoration: none;
    text-transform: uppercase;
    text-shadow: 0 1px 0 rgba(255,255,255,.8);
    white-space: nowrap;
  }
  .nav-services { left: 175px; width: 152px; color: var(--nav-light); font-weight: 600; }
  .nav-about { left: 845px; width: 162px; color: var(--nav-dark); }
  .brand-mark {
    position: absolute;
    left: 516px; top: 262px;
    width: 156px; height: 156px;
    border-radius: 50%;
    background: var(--brand-mark);
  }
  .brand-name {
    position: absolute;
    left: 0; right: 0; top: 488px;
    text-align: center;
    font-size: 68px;
    font-weight: 700;
    line-height: 1;
    color: var(--brand);
    text-transform: uppercase;
    letter-spacing: -2px;
    padding-left: 8px;
  }
</style>
</head>
<body>
  <nav class="language-tab" aria-label="Language">
    <a href="#" aria-label="English">
      <svg viewBox="0 0 60 30" preserveAspectRatio="none">
        <rect width="60" height="30" fill="var(--flag-blue)"/>
        <path d="M0 0L60 30M60 0L0 30" stroke="var(--flag-white)" stroke-width="6"/>
        <path d="M0 0L60 30M60 0L0 30" stroke="var(--flag-red)" stroke-width="2"/>
        <path d="M30 0V30M0 15H60" stroke="var(--flag-white)" stroke-width="10"/>
        <path d="M30 0V30M0 15H60" stroke="var(--flag-red)" stroke-width="6"/>
      </svg>
    </a>
    <a href="#" aria-label="Chinese">
      <svg viewBox="0 0 30 20" preserveAspectRatio="none">
        <rect width="30" height="20" fill="var(--flag-red)"/>
        <polygon points="5,2 5.9,4.7 8.8,4.7 6.5,6.4 7.3,9.1 5,7.5 2.7,9.1 3.5,6.4 1.2,4.7 4.1,4.7" fill="var(--flag-yellow)"/>
        <circle cx="10" cy="2" r="0.8" fill="var(--flag-yellow)"/>
        <circle cx="12" cy="4" r="0.8" fill="var(--flag-yellow)"/>
        <circle cx="12" cy="7" r="0.8" fill="var(--flag-yellow)"/>
        <circle cx="10" cy="9" r="0.8" fill="var(--flag-yellow)"/>
      </svg>
    </a>
    <a href="#" aria-label="Japanese">
      <svg viewBox="0 0 30 20" preserveAspectRatio="none">
        <rect width="30" height="20" fill="var(--flag-white)"/>
        <circle cx="15" cy="10" r="6" fill="var(--flag-red)"/>
      </svg>
    </a>
  </nav>

  <nav class="main-nav" aria-label="Main">
    <a class="nav-services" href="#">Services</a>
    <a class="nav-about" href="#">About Us</a>
  </nav>

  <div class="brand">
    <div class="brand-mark"></div>
    <div class="brand-name">Corvalt</div>
  </div>
</body>
</html>
```